New Solo Law Office Needs Business Card/Letterhead Design

I am starting a solo law office called "Law Office of Conrad Vashti, PLLC" in Tucson, Arizona. I will be doing criminal defense trial work. More than a logo with any sort of icon, I am really just looking for the name of the company to be displayed in a sleek, minimalist but interesting sort of way, with a format and font type that communicates professionalism. It can be in color, but doesn't have to be, and I am thinking blue and/or red accents colors. I'd like it to convey that I am passionate, dependable and willing to fight. For the business card, I envision sort of higher quality card material, and maybe some embossing or raised print. I will want to include my company name, name, phone and fax numbers, email and website addresses. For the letterhead, I will want to be able to use the same sort of font/formatting design as on the business card.
Industry/Entity Type
Business
Contact Information for Business Card
Law Office of Conrad Vashti, PLLC
Conrad Vashti
conrad@vashti-law.example
www.vashti-law.example
(I do not yet have an established phone or fax number, so please put in some place holder numbers for the formatting, and I can add the actual numbers in before I print.)
Colors
Designer to choose colors to be used in the design.
Look and feel

```html
<!DOCTYPE html>
<html lang="en">
<head>
<meta charset="utf-8">
<title>Law Office of Conrad Vashti, PLLC – Business Card</title>
<link rel="stylesheet" href="https://fonts.googleapis.com/css2?family=Raleway:wght@500;600;700&family=Open+Sans:wght@400&display=swap">
<style>
  :root {
    --card-blue: #23418e;
    --emblem-blue: #3a5cb8;
    --emblem-soft: #2c4da3;
    --ink-white: #ffffff;
  }
  html, body {
    margin: 0;
    padding: 0;
    width: 1200px;
    height: 686px;
    overflow: hidden;
    background: var(--card-blue);
  }
  .business-card {
    position: relative;
    width: 1200px;
    height: 686px;
    background: var(--card-blue);
    color: var(--ink-white);
    font-family: "Raleway", sans-serif;
  }
  .attorney-name {
    position: absolute;
    left: 77px;
    top: 80px;
    margin: 0;
    font-size: 58px;
    font-weight: 700;
    letter-spacing: 0.5px;
    line-height: 1;
  }
  .attorney-title {
    position: absolute;
    left: 78px;
    top: 150px;
    margin: 0;
    font-size: 25px;
    font-weight: 700;
    letter-spacing: 1.6px;
  }
  .firm-name {
    position: absolute;
    left: 77px;
    top: 299px;
    margin: 0;
    font-size: 38px;
    font-weight: 600;
    line-height: 1;
  }
  .contact-list {
    position: absolute;
    left: 77px;
    top: 364px;
    margin: 0;
    padding: 0;
    list-style: none;
  }
  .contact-item {
    display: flex;
    align-items: center;
    height: 40px;
    margin-bottom: 14px;
  }
  .contact-icon {
    width: 40px;
    height: 40px;
    margin-right: 13px;
    flex: none;
  }
  .contact-text {
    font-size: 33px;
    font-weight: 500;
  }
  .contact-text.number {
    font-family: "Open Sans", sans-serif;
    font-weight: 400;
    font-size: 32px;
  }
  .emblem-area {
    position: absolute;
    left: 775px;
    top: 189px;
    width: 391px;
    height: 314px;
    border-radius: 50% 50% 46% 46%;
    background: radial-gradient(ellipse at center, var(--emblem-blue) 0%, var(--emblem-soft) 55%, var(--card-blue) 100%);
  }
</style>
</head>
<body>
<main class="business-card">
  <h1 class="attorney-name">CONRAD VASHTI</h1>
  <p class="attorney-title">Designation here</p>

  <h2 class="firm-name">Law Office of Conrad Vashti, PLLC</h2>

  <ul class="contact-list">
    <li class="contact-item">
      <svg class="contact-icon" viewBox="0 0 40 40" aria-label="Phone">
        <circle cx="20" cy="20" r="18.5" fill="none" stroke="#fff" stroke-width="2"/>
        <path d="M14 10c1.5-1 2.5-.5 3.2 1l1.5 3.2c.4 1 .1 1.8-.7 2.4l-1.2.9c.8 2.4 2.6 4.6 4.8 6l1.2-.9c.8-.6 1.7-.6 2.4.1l2.6 2.4c1 .9 1 2-.1 3l-1.5 1.3c-5.5 2-14.5-8.5-13.6-15.3z" fill="#fff"/>
      </svg>
      <span class="contact-text number">91-55501473</span>
    </li>
    <li class="contact-item">
      <svg class="contact-icon" viewBox="0 0 40 40" aria-label="Fax">
        <circle cx="20" cy="20" r="18.5" fill="none" stroke="#fff" stroke-width="2"/>
        <rect x="14" y="10" width="12" height="6" fill="#fff"/>
        <rect x="10" y="16" width="20" height="10" rx="2" fill="#fff"/>
        <rect x="14" y="22" width="12" height="8" fill="#fff" stroke="#23418e" stroke-width="1.5"/>
        <line x1="16" y1="25" x2="24" y2="25" stroke="#23418e" stroke-width="1.2"/>
        <line x1="16" y1="27.5" x2="24" y2="27.5" stroke="#23418e" stroke-width="1.2"/>
      </svg>
      <span class="contact-text number">231-5550194</span>
    </li>
    <li class="contact-item">
      <svg class="contact-icon" viewBox="0 0 40 40" aria-label="Email">
        <circle cx="20" cy="20" r="18.5" fill="none" stroke="#fff" stroke-width="2"/>
        <rect x="10" y="13" width="20" height="14" fill="#fff"/>
        <path d="M10 13l10 8 10-8" fill="none" stroke="#23418e" stroke-width="1.5"/>
      </svg>
      <span class="contact-text">conrad@vashti-law.example</span>
    </li>
    <li class="contact-item">
      <svg class="contact-icon" viewBox="0 0 40 40" aria-label="Website">
        <circle cx="20" cy="20" r="18.5" fill="none" stroke="#fff" stroke-width="2"/>
        <circle cx="20" cy="20" r="11" fill="none" stroke="#fff" stroke-width="1.6"/>
        <ellipse cx="20" cy="20" rx="5" ry="11" fill="none" stroke="#fff" stroke-width="1.4"/>
        <line x1="9" y1="20" x2="31" y2="20" stroke="#fff" stroke-width="1.4"/>
        <line x1="11" y1="15" x2="29" y2="15" stroke="#fff" stroke-width="1.2"/>
        <line x1="11" y1="25" x2="29" y2="25" stroke="#fff" stroke-width="1.2"/>
      </svg>
      <span class="contact-text">www.vashti-law.example</span>
    </li>
  </ul>

  <div class="emblem-area" role="img" aria-label="Embossed emblem of the scales of justice framed by a laurel wreath"></div>
</main>
</body>
</html>
```